Kelpline Aquatics Website and inner template.

New website design for an existing client. Need a home page design and a simplified inner page template design, I have included a txt document with the specifics for this website design/poject. I have copy and pasted the info below
Project Description: Website design ( home page with an inner page template ) for Kelpline Aquatics LLC
Current Website Address: https://kelplineaquatics.example
Main navigation link: ( same as on current website with the exception of Links and Resources being removed )
Instruction/Courses
Rentals
Trips & Charters
Service & Repairs
Tank Fills
Home
Contact
About ( Company Info )
Events
Specials
Home page specifics:
As with all website lately, they requested a large "hero banner" or "slider image" above the fold just below the navigation. Examples
https://harrowmetalworks.example/
https://pinfernstudio.example/
https://lomasparrowfield.example/
In addition to the main navigation menu and hero banner, we need to highlight some important features/links on the home page
Social media icons for facebook and instagram
Store Hours
Contact Information in cluding phone numbers
Scuba Instruction/Courses Link highlight area
Scuba Rental Gear Link highlight area
Scuba Repair Service Link highlight area
Large content area. Needs to be large enoug to move over the existing content on the current website ( see link above )
Large section for "Snorkels, Masks, Fins - How to Fit & Care for them " . Currently that is the only page on the resources page. Since we are removing the resources page, we would like make this a stand alone page only accessible via the home page in a highlight area.
Other Notes:
I have attached the logo to the project.
IMPORTANT... ONLY USE GRAPHICS/IMAGES from plenta image. ( https://www.plentaimage.example/ ) This is important because we have an account with them so you can use the watermarked images then when I build the website I can easily purchase the licensing rights for those images. You dont' need an account to do searches, locate images and use the water marked image in the design.
Target Market(s)
Diving Lessons, Equipment repair and charters
Number of Pages Required
2 page
Requirements
Must have
- Please see attached txt document with all the project specifics
Nice to have
Should not have

```html
<!DOCTYPE html>
<html lang="en">
<head>
<meta charset="utf-8">
<title>Kelpline Aquatics LLC</title>
<link href="https://fonts.googleapis.com/css2?family=Roboto:wght@400;500;700;900&display=swap" rel="stylesheet">
<style>
:root{
  --red:#d6262e;
  --navy:#0d1c28;
  --navy-2:#13283a;
  --teal:#0e3d55;
  --ink:#222;
  --muted:#666;
  --grey-bg:#f1f1f1;
  --line:#e2e2e2;
  --white:#fff;
}
*{box-sizing:border-box;margin:0;padding:0}
html,body{width:1200px;height:2816px;overflow:hidden}
body{font-family:"Roboto",sans-serif;color:var(--ink);background:var(--white);position:relative}
.abs{position:absolute}

/* header */
.site-header{position:absolute;left:0;top:0;width:1200px;height:108px;background:var(--white)}
.brand{left:112px;top:22px;display:flex;align-items:center;gap:12px}
.brand-mark{width:44px;height:34px;background:var(--red)}
.brand-name{font-weight:700;font-size:26px;color:var(--red);letter-spacing:.5px}
.top-info{top:12px;display:flex;align-items:center;gap:10px}
.top-info .ico{width:34px;height:34px;border:2px solid var(--red);border-radius:50%;display:flex;align-items:center;justify-content:center}
.top-info small{display:block;font-size:11px;color:var(--muted)}
.top-info b{font-size:14px;font-weight:700;color:var(--ink)}
.main-nav{left:560px;top:62px;display:flex;gap:0}
.main-nav a{font-size:14px;font-weight:700;color:var(--ink);text-decoration:none;padding:6px 14px}
.main-nav a.active{color:var(--red);border-bottom:3px solid var(--red)}
.socials{left:1010px;top:62px;display:flex;gap:10px}
.socials span{width:28px;height:28px;border-radius:50%;border:1px solid #ccc;display:block}

.sub-nav{position:absolute;left:112px;top:108px;width:976px;height:40px;background:var(--teal);display:flex;z-index:2}
.sub-nav a{flex:1;color:var(--white);font-size:14px;font-weight:700;text-decoration:none;display:flex;align-items:center;justify-content:center;text-transform:uppercase}
.sub-nav a.hl{background:var(--red)}

/* hero */
.hero{position:absolute;left:0;top:144px;width:1200px;height:608px;background:linear-gradient(180deg,#0a3d6e 0%,#0f6a9c 45%,#16839f 75%,#0c4f6b 100%)}
.hero-copy{left:112px;top:196px;width:440px;color:var(--white)}
.hero-copy h1{font-size:44px;font-weight:900;text-transform:uppercase;margin-bottom:14px}
.hero-copy p{font-size:16px;font-weight:500;line-height:1.45;margin-bottom:22px}
.btn-ghost{display:inline-block;border:2px solid var(--white);border-radius:22px;padding:10px 22px;color:var(--white);font-size:13px;font-weight:700;text-transform:uppercase}
.hero-arrow{top:260px;width:36px;height:36px;border-radius:50%;background:var(--white);display:flex;align-items:center;justify-content:center}

/* feature cards */
.card{top:688px;width:300px;height:292px;background:var(--white);box-shadow:0 4px 18px rgba(0,0,0,.15);text-align:center;padding:36px 26px 0}
.card.dark{background:var(--navy);color:var(--white)}
.card h3{font-size:22px;font-weight:700;color:var(--red);text-transform:uppercase;margin:18px 0 12px}
.card p{font-size:13px;line-height:1.5;color:var(--muted)}
.card.dark p{color:#cfd6dc}

/* content */
.content-band{position:absolute;left:0;top:1020px;width:1200px;height:1160px;background:var(--grey-bg)}
.photo{border-radius:4px}
.story{width:440px}
.story h2{font-size:26px;font-weight:900;text-transform:uppercase;margin-bottom:18px}
.story p{font-size:14px;line-height:1.65;color:var(--muted);margin-bottom:24px}
.btn-red{display:inline-block;background:var(--red);color:var(--white);font-size:13px;font-weight:700;text-transform:uppercase;padding:12px 22px;border-radius:22px}

/* partners */
.partners-title{left:0;top:2288px;width:1200px;text-align:center;font-size:36px;font-weight:900;text-transform:uppercase}
.partner{top:2360px;width:216px;height:88px;border:1px solid var(--line);border-radius:44px;display:flex;align-items:center;justify-content:center}
.partner span{display:block;border-radius:6px}

/* footer */
.site-footer{position:absolute;left:0;top:2520px;width:1200px;height:240px;background:var(--navy)}
.foot-col{top:36px;color:#c9d1d8;font-size:13px}
.foot-col h4{color:var(--white);font-size:15px;font-weight:700;text-transform:uppercase;padding-bottom:8px;margin-bottom:12px;border-bottom:2px solid var(--red);display:inline-block}
.foot-col li{list-style:none;line-height:1.75}
.contact-list li{display:flex;gap:8px;align-items:center}
.bottom-bar{position:absolute;left:0;top:2760px;width:1200px;height:56px;background:var(--white);display:flex;align-items:center;justify-content:space-between;padding:0 112px;font-size:12px;color:var(--muted)}
.bottom-bar .soc{display:flex;gap:10px}
.bottom-bar .soc span{width:26px;height:26px;border-radius:50%;background:var(--red);display:block}
</style>
</head>
<body>

<header class="site-header">
  <div class="abs brand"><span class="brand-mark"></span><span class="brand-name">KELPLINE AQUATICS, LLC</span></div>

  <div class="abs top-info" style="left:790px">
    <span class="ico"><svg width="16" height="16" viewBox="0 0 24 24"><path d="M6.6 10.8a15 15 0 006.6 6.6l2.2-2.2c.3-.3.7-.4 1-.2 1.1.4 2.3.6 3.6.6.6 0 1 .4 1 1V20c0 .6-.4 1-1 1A17 17 0 013 4c0-.6.4-1 1-1h3.5c.6 0 1 .4 1 1 0 1.2.2 2.4.6 3.6.1.3 0 .7-.2 1z" fill="#d6262e"/></svg></span>
    <div><small>Call Us</small><b>(555) 014-2290</b></div>
  </div>
  <div class="abs top-info" style="left:950px">
    <span class="ico"><svg width="16" height="16" viewBox="0 0 24 24"><circle cx="12" cy="12" r="9" fill="none" stroke="#d6262e" stroke-width="2"/><path d="M12 7v5l3 3" stroke="#d6262e" stroke-width="2" fill="none"/></svg></span>
    <div><small>Store Hours</small><b>Mon-Sat: 10am-6pm</b></div>
  </div>

  <nav class="abs main-nav">
    <a class="active">HOME</a><a>ABOUT</a><a>EVENTS</a><a>SPECIALS</a><a>CONTACT</a>
  </nav>
  <div class="abs socials"><span></span><span></span></div>
</header>

<nav class="sub-nav">
  <a>Instruction/Courses</a><a>Rentals</a><a>Trips &amp; Charters</a><a class="hl">Service &amp; Repairs</a><a>Tank Fills</a>
</nav>

<section class="hero" role="img" aria-label="Scuba divers swimming over a coral reef in blue water">
  <div class="abs hero-copy">
    <h1>Welcome to Kelpline Aquatics</h1>
    <p>Welcome to Kelpline Aquatics, a scuba and snorkeling shop located in the beautiful town of Millbrook Connecticut</p>
    <span class="btn-ghost">View Our Work</span>
  </div>
  <div class="abs hero-arrow" style="left:28px"><svg width="12" height="12" viewBox="0 0 12 12"><path d="M8 1L3 6l5 5" stroke="#0d1c28" stroke-width="2" fill="none"/></svg></div>
  <div class="abs hero-arrow" style="left:1136px"><svg width="12" height="12" viewBox="0 0 12 12"><path d="M4 1l5 5-5 5" stroke="#0d1c28" stroke-width="2" fill="none"/></svg></div>
</section>

<article class="abs card" style="left:144px">
  <svg width="44" height="44" viewBox="0 0 44 44"><circle cx="22" cy="10" r="5" fill="#0d1c28"/><path d="M10 34l12-14 12 14M22 20v-4" stroke="#0d1c28" stroke-width="3" fill="none"/></svg>
  <h3>Scuba Courses</h3>
  <p>From the North Atlantic waters off the coast of New England to the sand-rimmed shallows of Coral Point, learn with us.</p>
</article>
<article class="abs card dark" style="left:450px">
  <svg width="44" height="44" viewBox="0 0 44 44"><rect x="8" y="14" width="28" height="16" rx="6" fill="none" stroke="#fff" stroke-width="3"/><path d="M22 14v16" stroke="#fff" stroke-width="3"/></svg>
  <h3>Rental Gears</h3>
  <p>Kelpline Aquatics has a full line of scuba equipment available for rental, just because you haven't purchased your own equipment.</p>
</article>
<article class="abs card" style="left:756px">
  <svg width="44" height="44" viewBox="0 0 44 44"><path d="M12 32l16-16M26 10a6 6 0 008 8l-4 4-8-8z" stroke="#0d1c28" stroke-width="3" fill="none"/></svg>
  <h3>Repair Service</h3>
  <p>Our fully trained and certified technicians are ready to service your scuba equipment for all divers.</p>
</article>

<section class="content-band">
  <div class="abs photo" style="left:112px;top:92px;width:488px;height:328px;background:linear-gradient(160deg,#2a8fb8,#0d5a80)" role="img" aria-label="Rescue divers training together underwater"></div>
  <div class="abs story" style="left:644px;top:112px">
    <h2>Rescue &amp; Commercial</h2>
    <p>Our rescue and commercial programs prepare divers for real work below the surface. Train with experienced instructors in controlled settings, learn search patterns, victim recovery and surface support, then build the skills and confidence needed for professional dive assignments and crew roles.</p>
    <span class="btn-red">Learn More</span>
  </div>

  <div class="abs story" style="left:112px;top:452px">
    <h2>Scuba &amp; Exotic Travel</h2>
    <p>Join our group trips to warm reefs and distant islands. We plan the charters, lodging and dive schedules so you can focus on the water. Every trip is led by our staff, with small groups, daily boat dives and plenty of time to explore.</p>
    <span class="btn-red">Learn More</span>
  </div>
  <div class="abs photo" style="left:600px;top:420px;width:488px;height:340px;background:linear-gradient(170deg,#37b3cf,#0f7895)" role="img" aria-label="Snorkelers swimming near a reef in clear water"></div>

  <div class="abs photo" style="left:112px;top:760px;width:488px;height:340px;background:linear-gradient(165deg,#3fa7b0,#0e6a74)" role="img" aria-label="Sea turtle swimming over a shallow reef"></div>
  <div class="abs story" style="left:644px;top:790px">
    <h2>Snorkeling &amp; Swimming</h2>
    <p>Snorkels, masks and fins: learn how to choose, fit and care for them. Our guide covers strap adjustment, mask seals, fin sizing, rinsing after salt water and storage tips, so your gear stays comfortable and lasts for many seasons.</p>
    <span class="btn-red">Learn More</span>
  </div>
</section>

<h2 class="abs partners-title">Our Partners</h2>
<div class="abs partner" style="left:112px"><span style="width:120px;height:44px;background:#1f5f8e"></span></div>
<div class="abs partner" style="left:366px"><span style="width:140px;height:36px;background:#3a3a3a"></span></div>
<div class="abs partner" style="left:620px"><span style="width:120px;height:44px;background:#2b4fa3"></span></div>
<div class="abs partner" style="left:872px"><span style="width:60px;height:60px;border-radius:50%;background:#2f8fc4"></span></div>

<footer class="site-footer">
  <div class="abs foot-col" style="left:112px">
    <h4>Company</h4>
    <ul><li>Home</li><li>About</li><li>Events</li><li>Specials</li><li>Contact</li></ul>
  </div>
  <div class="abs foot-col" style="left:350px">
    <h4>Useful Links</h4>
    <ul><li>Instruction/Courses</li><li>Rentals</li><li>Trips &amp; Charters</li><li>Service &amp; Repairs</li><li>Tank Fills</li></ul>
  </div>
  <div class="abs foot-col" style="left:620px">
    <h4>About</h4>
    <ul><li>Site Map</li><li>Privacy Policy</li><li>Terms Of Use</li></ul>
  </div>
  <div class="abs foot-col" style="left:860px">
    <h4>Contact Us</h4>
    <ul class="contact-list">
      <li><svg width="12" height="14" viewBox="0 0 12 14"><path d="M6 0a5 5 0 015 5c0 4-5 9-5 9S1 9 1 5a5 5 0 015-5z" fill="#d6262e"/></svg>Kelpline Aquatics 12 Harbor Row<br>Millbrook, CT 06900</li>
      <li><svg width="12" height="12" viewBox="0 0 24 24"><path d="M6.6 10.8a15 15 0 006.6 6.6l2.2-2.2c.3-.3.7-.4 1-.2 1.1.4 2.3.6 3.6.6.6 0 1 .4 1 1V20c0 .6-.4 1-1 1A17 17 0 013 4c0-.6.4-1 1-1h3.5c.6 0 1 .4 1 1 0 1.2.2 2.4.6 3.6z" fill="#d6262e"/></svg>(555) 014-2290</li>
      <li><svg width="12" height="12" viewBox="0 0 24 24"><path d="M6.6 10.8a15 15 0 006.6 6.6l2.2-2.2c.3-.3.7-.4 1-.2 1.1.4 2.3.6 3.6.6.6 0 1 .4 1 1V20c0 .6-.4 1-1 1A17 17 0 013 4c0-.6.4-1 1-1h3.5c.6 0 1 .4 1 1 0 1.2.2 2.4.6 3.6z" fill="#d6262e"/></svg>(555) 014-7731</li>
      <li><svg width="12" height="12" viewBox="0 0 24 24"><circle cx="12" cy="12" r="9" fill="none" stroke="#d6262e" stroke-width="3"/></svg>Mon-Sat: 10am-6pm</li>
    </ul>
  </div>
</footer>

<div class="bottom-bar">
  <span>Copyright 2021 KELPLINE AQUATICS LLC. All rights reserved.</span>
  <div class="soc"><span></span><span></span></div>
</div>

</body>
</html>
```